Telecom company needs marketing flyers

We need 3 different flyers to describe our product and how to qualify for the program. This our website to use for the logo and color scheme https://www.brivolinkmobile.com, however do not use the mascot on the flyer.

Attached are examples of a competitors flyers.

```html
<!DOCTYPE html>
<html lang="en">
<head>
<meta charset="utf-8">
<title>Brivolink Mobile – Flyer Set</title>
<link href="https://fonts.googleapis.com/css2?family=Raleway:wght@300;400;500;600&family=Rubik:wght@700;800&display=swap" rel="stylesheet">
<style>
:root{
  --blue:#1aa7e4;
  --teal:#1ec3bd;
  --sky:#d2eaf4;
  --ink:#333a40;
  --stage:#a4a6a9;
  --white:#ffffff;
}
*{box-sizing:border-box;margin:0;padding:0}
html,body{width:1200px;height:528px;overflow:hidden;background:var(--stage)}
body{position:relative;font-family:"Raleway",sans-serif;color:var(--ink)}
.page{position:absolute;top:28px;width:361px;height:468px;background:var(--white);overflow:hidden;box-shadow:3px 4px 8px rgba(0,0,0,.3)}
.page--tablet{left:27px}
.page--benefit{left:422px}
.page--qualify{left:814px}
.abs{position:absolute}
.bg{position:absolute;inset:0}

/* brand name */
.brand{position:absolute;color:var(--blue);font-family:"Raleway",sans-serif;font-weight:500;line-height:1}
.brand__name{display:block;font-size:16px;letter-spacing:2.2px}
.brand__sub{display:block;font-size:5.4px;letter-spacing:2px;text-align:right;margin-top:3px}

/* shared */
.band{position:absolute;background:var(--teal);color:var(--white);white-space:nowrap}
.heavy{font-family:"Rubik",sans-serif;font-weight:800;color:var(--blue)}
.fine{position:absolute;font-size:3.4px;line-height:4.1px;color:var(--ink);text-align:justify}
.photo{position:absolute}

/* page 1 */
.limited{left:0;top:61px;width:168px;height:25px;border-radius:0 12px 0 0;font-size:13px;font-weight:500;padding:5px 0 0 9px;letter-spacing:.2px}
.tablet{left:20px;top:107px;width:177px;height:291px;background:#1d1f22;border-radius:12px;padding:13px 11px 13px 12px}
.tablet__screen{width:100%;height:100%;background:linear-gradient(180deg,#e9f3f7 0%,#c3dde8 45%,#5f9fb5 80%,#2f6377 100%)}
.offer{left:206px;top:125px;font-size:26px;line-height:25.5px}
.offer sup{font-size:13px;position:relative;top:-11px;line-height:0;vertical-align:baseline}
.offer-note{left:208px;top:238px;font-size:7.6px;font-weight:600;color:var(--teal);white-space:nowrap}
.feature{position:absolute;left:208px;width:150px}
.feature__icon{position:absolute;left:0;top:0;width:22px;height:22px}
.feature__text{position:absolute;left:27px;top:1px;width:118px;font-size:6.4px;line-height:7.6px}
.dealer{left:211px;top:384px;width:150px;height:17px;border-radius:8px 0 0 0;font-size:7.3px;font-weight:600;padding:3px 0 0 9px}

/* page 2 */
.free{left:30px;top:86px;font-size:25.5px;letter-spacing:.3px}
.programs{left:30px;top:113px;font-size:14px;line-height:17.3px;font-weight:400;color:var(--teal)}
.unlimited{left:0;width:361px;text-align:center;font-size:27px;line-height:31px}
.ask{left:17px;top:321px;width:334px;height:40px;border-radius:0 14px 0 0;display:flex;align-items:center}
.ask__left{width:92px;text-align:center;font-size:12.5px;line-height:14.5px;font-weight:400}
.ask__rule{width:1px;height:30px;background:var(--white)}
.ask__right{padding-left:8px;font-size:13.5px;line-height:15.5px;font-weight:400}

/* page 3 */
.notice{left:27px;top:44px;width:319px;height:19px;font-size:6.6px;letter-spacing:1.7px;padding:5px 0 0 10px;font-weight:500;overflow:hidden}
.need{left:14px;top:90px;width:74px;text-align:right;font-size:10.5px;line-height:13px;color:var(--teal);font-weight:400}
.id-card{left:109px;top:70px;width:118px;height:78px;border-radius:4px;background:linear-gradient(135deg,#c7c8e6 0%,#e6e2ea 50%,#cfd6ea 100%);box-shadow:1px 2px 3px rgba(0,0,0,.3)}
.id-note{left:236px;top:130px;font-size:6px;line-height:7.5px}
.qualify-title{left:0;top:177px;width:361px;text-align:center;font-size:15.5px}
.qualify-title sup{font-size:7px;position:relative;top:-6px;line-height:0;vertical-align:baseline}
.qualify-list{left:0;top:201px;width:361px;text-align:center;font-size:6.8px;line-height:8.3px}
.rule-box{position:absolute;top:242px;width:105px;height:87px;color:var(--white);text-align:center;padding:6px 5px 0}
.rule-box--phone{left:17px;background:var(--blue);border-radius:16px 0 16px 0}
.rule-box--house{left:128px;background:var(--teal);border-radius:0 16px 0 16px}
.rule-box--renew{left:241px;background:var(--blue);border-radius:16px 0 0 16px}
.rule-box h3{font-size:6.4px;font-weight:500;margin-bottom:3px;letter-spacing:.2px}
.rule-box p{font-size:4.7px;line-height:5.6px}
.visit{left:14px;top:414px;width:333px;height:19px;border-radius:10px;text-align:center;font-size:10.5px;padding-top:3px;font-weight:400}
</style>
</head>
<body>

<!-- Flyer 1: tablet offer -->
<section class="page page--tablet">
  <svg class="bg" viewBox="0 0 361 468" preserveAspectRatio="none" aria-hidden="true">
    <path d="M0 0H361V140C320 130 290 128 262 142C226 160 205 178 176 178C140 178 118 150 60 148C35 147 15 150 0 154Z" fill="var(--sky)"/>
  </svg>
  <div class="brand" style="left:9px;top:22px"><span class="brand__name">BRIVOLINK</span><span class="brand__sub">MOBILE</span></div>
  <div class="band limited">FOR A LIMITED TIME</div>
  <div class="abs tablet"><div class="tablet__screen" role="img" aria-label="Tablet screen showing a bright stadium with a glowing teal runner"></div></div>
  <h1 class="abs heavy offer">Get an<br>8” tablet<br>for just<br><sup>$</sup>10.01!</h1>
  <p class="abs offer-note">This special offer won’t last forever!</p>

  <div class="feature" style="top:254px">
    <svg class="feature__icon" viewBox="0 0 24 24" aria-hidden="true"><circle cx="12" cy="12" r="11" fill="none" stroke="var(--teal)" stroke-width="1.5"/><circle cx="12" cy="12" r="8.5" fill="var(--teal)"/><path d="M7 12.2 17 7.5 14.2 17 11.6 13.3Z" fill="var(--white)"/></svg>
    <p class="feature__text">More data means more email, more video conferencing, more Internet!</p>
  </div>
  <div class="feature" style="top:284px">
    <svg class="feature__icon" viewBox="0 0 24 24" aria-hidden="true"><circle cx="12" cy="12" r="11" fill="none" stroke="var(--teal)" stroke-width="1.5"/><circle cx="12" cy="12" r="8.5" fill="var(--teal)"/><path d="M7.5 10.5a6.5 6.5 0 0 1 9 0M9.2 12.3a4 4 0 0 1 5.6 0" fill="none" stroke="var(--white)" stroke-width="1.2" stroke-linecap="round"/><circle cx="12" cy="14.6" r="1.1" fill="var(--white)"/></svg>
    <p class="feature__text" style="top:7px">Fast, flexible 5G Network.</p>
  </div>
  <div class="feature" style="top:313px">
    <svg class="feature__icon" viewBox="0 0 24 24" aria-hidden="true"><circle cx="12" cy="12" r="11" fill="none" stroke="var(--teal)" stroke-width="1.5"/><circle cx="12" cy="12" r="8.5" fill="var(--teal)"/><rect x="9.3" y="6.5" width="5.4" height="11" rx="1" fill="none" stroke="var(--white)" stroke-width="1.1"/><circle cx="12" cy="15.6" r=".6" fill="var(--white)"/></svg>
    <p class="feature__text">Mobile hotspot included means you can connect other devices to your Crestline Service.</p>
  </div>
  <div class="feature" style="top:344px">
    <svg class="feature__icon" viewBox="0 0 24 24" aria-hidden="true"><circle cx="12" cy="12" r="11" fill="none" stroke="var(--teal)" stroke-width="1.5"/><circle cx="12" cy="12" r="8.5" fill="var(--teal)"/><path d="M12 10.5 9.5 17.5M12 10.5 14.5 17.5M8.6 7.6a4.8 4.8 0 0 0 0 6.3M15.4 7.6a4.8 4.8 0 0 1 0 6.3" fill="none" stroke="var(--white)" stroke-width="1.1" stroke-linecap="round"/><circle cx="12" cy="10.6" r="1.2" fill="var(--white)"/></svg>
    <p class="feature__text">Cellular Connectivity lets you take internet anywhere there is coverage.</p>
  </div>

  <div class="band dealer">See your authorized dealer for info!</div>
  <p class="fine" style="left:13px;top:411px;width:335px">Promotional offer subject to eligibility for the Emergency Broadband Benefit (EBB). The EBB is a temporary federal program that provides non-transferable discounts on monthly broadband service. Only one benefit is allowed per household. Benefits may be moved to another provider at any time. When the program ends, you will return to standard Lifeline service unless you opt out. Visit our website or call us for details on eligibility and fees.</p>
</section>

<!-- Flyer 2: benefit programs -->
<section class="page page--benefit">
  <svg class="bg" viewBox="0 0 361 468" preserveAspectRatio="none" aria-hidden="true">
    <path d="M146 30C170 6 230 2 290 14C330 22 361 40 361 40V250H250C215 250 190 230 175 200C160 170 140 150 140 110C140 80 130 55 146 30Z" fill="var(--sky)"/>
    <path d="M0 215C20 212 38 220 40 236C42 248 36 254 28 256H0Z" fill="var(--sky)"/>
  </svg>
  <div class="brand" style="left:27px;top:37px"><span class="brand__name">BRIVOLINK</span><span class="brand__sub">MOBILE</span></div>
  <h1 class="abs heavy free">FREE</h1>
  <p class="abs programs">Lifeline and<br>Emergency<br>Broadband<br>Benefit<br>Programs</p>
  <div class="photo" style="left:150px;top:37px;width:211px;height:212px;border-radius:60px 0 0 30px;background:linear-gradient(160deg,#c99a7a 0%,#9fb4c4 45%,#e3613e 75%,#5c6670 100%)" role="img" aria-label="Photo of a father and daughter smiling while using a tablet together"></div>
  <h2 class="abs heavy unlimited" style="top:256px">Unlimited Talk &amp; Text</h2>
  <h2 class="abs heavy unlimited" style="top:288px">+ 10 GB of Data</h2>
  <div class="band ask">
    <div class="ask__left">Ask if you<br>Qualify!</div>
    <div class="ask__rule"></div>
    <div class="ask__right">www.brivolinkmobile.com<br>+800-555-0142</div>
  </div>
  <p class="fine" style="left:17px;top:368px;width:334px;font-size:3.9px;line-height:4.6px">Promotional offer subject to eligibility for the Emergency Broadband Benefit (EBB). Unlimited does not mean unreasonable use; see the Acceptable Use Policy in our Terms and Conditions for details. The EBB is a temporary federal program that provides non-transferable discounts on monthly broadband internet access service. Lifeline is a government assistance program that provides non-transferable discounts on your monthly phone or broadband service. Proof of eligibility is required, and only eligible customers may enroll. An eligible household is limited to one monthly service discount for Lifeline and one for EBB. Eligible consumers may get EBB service from Crestline Wireless or from any participating provider. Benefits may be transferred to another provider at any time. When the federal program ends or we end our promotional free EBB service offer, we will notify you and you will revert to receiving only the standard free Lifeline plan if you are eligible, or you may keep your EBB service by paying the applicable undiscounted rate plus fees and taxes. Lifeline plans may include 1,000 minutes, unlimited text, and 4.5 GB of data. Offers vary by state and service may not be available in all areas. Consumers who willfully make false statements in order to obtain Lifeline or EBB benefits can be punished by fine, imprisonment, or being barred from the program. Unresolved questions or complaints may be directed to your local public utilities commission. Consumers with hearing or speech impairments may use a relay service to reach their state commission.</p>
</section>

<!-- Flyer 3: how to qualify -->
<section class="page page--qualify">
  <svg class="bg" viewBox="0 0 361 468" preserveAspectRatio="none" aria-hidden="true">
    <path d="M95 75C110 40 150 30 190 36C230 42 250 18 275 24C300 30 298 70 285 100C270 135 250 160 215 172C180 184 140 180 115 160C92 140 82 105 95 75Z" fill="var(--sky)"/>
  </svg>
  <div class="brand" style="right:15px;top:17px"><span class="brand__name">BRIVOLINK</span><span class="brand__sub">MOBILE</span></div>
  <div class="band notice">IMPORTANT INFORMATION. PLEASE READ CAREFULLY.</div>
  <p class="abs need">WHAT YOU<br>NEED<br>TO APPLY:</p>
  <div class="abs id-card" role="img" aria-label="Illustration of a sample state identification card"></div>
  <p class="abs id-note">Unexpired<br>Government Issued ID</p>
  <h2 class="abs heavy qualify-title">HOW TO QUALIFY<sup>*</sup></h2>
  <p class="abs qualify-list">Food Stamps – Supplemental Nutrition Assistance Program (SNAP) • Medicaid<br>Supplemental Security Income (SSI) • Federal Public Housing Assistance (Section 8)<br>Veterans Pension and Survivors Benefit<br>Income Eligibility (household income must be at or below 135% of the federal poverty line)</p>

  <div class="rule-box rule-box--phone">
    <h3>USE YOUR PHONE</h3>
    <p>FCC guidelines require that you use your phone every 30 days or Crestline Wireless will be required to de-enroll your Lifeline benefit. Use your Crestline Wireless service as your primary phone, every day, so you do not risk losing your Lifeline benefit. If you need more minutes, or data, additional airtime is available by calling 611.</p>
  </div>
  <div class="rule-box rule-box--house">
    <h3>ONE PER HOUSEHOLD</h3>
    <p>The Lifeline Assistance program is available for only one wireless or wireline account per household. Separate households that live at the same address are eligible, including residents of homeless shelters and nursing homes. Residents with temporary addresses are also eligible.</p>
  </div>
  <div class="rule-box rule-box--renew">
    <h3>RECERTIFY ANNUALLY</h3>
    <p>Lifeline participants must recertify annually so that they remain eligible for the program. If you do not complete the recertification process as required, you will be de-enrolled from the Lifeline program and your free service will no longer work.</p>
  </div>

  <div class="photo" style="left:0;top:346px;width:96px;height:58px;background:linear-gradient(135deg,#5f8ea3,#cfd9dd)" role="img" aria-label="Photo of a senior woman using her phone"></div>
  <div class="photo" style="left:97px;top:346px;width:93px;height:58px;background:linear-gradient(135deg,#7fa46a,#d9c9b0)" role="img" aria-label="Photo of a smiling family outdoors"></div>
  <div class="photo" style="left:191px;top:346px;width:93px;height:58px;background:linear-gradient(135deg,#c8ccc9,#8a9197)" role="img" aria-label="Photo of a multigenerational family together"></div>
  <div class="photo" style="left:285px;top:346px;width:76px;height:58px;background:linear-gradient(135deg,#3f6f84,#a9c3cf)" role="img" aria-label="Photo of a man working on a laptop"></div>

  <div class="band visit">Visit: www.brivolinkmobile.com | Call us: +800-555-0142</div>
  <p class="fine" style="left:14px;top:438px;width:333px;font-size:3.3px;line-height:3.9px">National Verifier may need proof of program participation or identity.<br>*This is a Lifeline service. Lifeline is a government assistance program. Your Lifeline benefit is non-transferable. Proof of eligibility is required, and only eligible customers may enroll. Only one Lifeline discount per household. Consumers who willfully make false statements in order to obtain the benefit can be punished by fine or imprisonment or barred from the program. Plans may include 1,000 minutes, unlimited text, and 4.5 GB of data. Offers vary by state and service may not be available in all areas. Northway Connect Inc. of America d/b/a Crestline Wireless.</p>
</section>

</body>
</html>
```